Profesional personal website needs design and business card

I need a business card with my professional name as a logo "Marlo Vitality" for my business. I am a Wellness Coach, consultant and trainer. So it should be professional, wellness oriented and modern.

Target Market(s)

Private clients, governments, corporations. Luxury and high market.

Industry/Entity Type

Health And Wellness

Contact Information for Business Card

Marlo Vitality should be the logo

Colors

Designer to choose colors to be used in the design.

Requirements
Must have
• Marlo Vitality
• Name: Tomás Arribal
• Wellness Coach, Consultant & Trainer.
• Website: www.marlovitality.example
• Phone:
• Spain (+34) 612 480 397
• (USA) +1 (555) 318 2046
Nice to have
• The most important is the design of "Marlo Vitality", as this is going to be my personal brand logo. It should be professional, wellness, high end and actual.
Should not have
• no golds, no baroque style..

```html
<!DOCTYPE html>
<html lang="en">
<head>
<meta charset="utf-8">
<title>Marlo Vitality — Business Cards</title>
<link rel="stylesheet" href="https://fonts.googleapis.com/css2?family=Barlow+Condensed:wght@500;600&family=Tinos&display=swap">
<style>
  :root {
    --ink: #000000;
    --paper: #ffffff;
    --sans: "Barlow Condensed", sans-serif;
    --serif: "Tinos", serif;
  }
  * { margin: 0; padding: 0; box-sizing: border-box; }
  html, body { width: 1200px; height: 750px; overflow: hidden; background: var(--paper); }
  .stage { position: relative; width: 1200px; height: 750px; color: var(--ink); }
  .abs { position: absolute; }

  .card { position: absolute; left: 321px; width: 558px; height: 298px; border: 6.5px solid var(--ink); background: var(--paper); }
  .card--front { top: 61px; }
  .card--back { top: 391px; }

  /* front */
  .brand-mark { left: 360px; top: 91px; width: 46px; height: 46px; border: 3px solid var(--ink); }
  .brand-name { font-family: var(--sans); font-weight: 600; text-transform: uppercase; line-height: 1.05; text-align: center; font-size: 14px; letter-spacing: 0.02em; }
  .brand-name--front { left: 343px; top: 143px; width: 80px; }
  .front-name { left: 400px; width: 400px; top: 197px; text-align: center; font-family: var(--sans); font-weight: 600; font-size: 25px; letter-spacing: 0.02em; line-height: 1; }
  .front-roles { left: 380px; width: 440px; top: 226px; text-align: center; font-family: var(--serif); font-size: 15px; text-transform: uppercase; }
  .front-contact { left: 390px; width: 440px; top: 260px; text-align: center; font-family: var(--sans); font-weight: 600; font-size: 12px; text-transform: uppercase; white-space: nowrap; }

  /* back */
  .edge-block { background: var(--ink); }
  .edge-block--left { left: 321px; top: 391px; width: 20px; height: 123px; }
  .edge-block--bottom { left: 757px; top: 669px; width: 121px; height: 20px; }
  .brand-name--back { left: 724px; top: 442px; width: 100px; }
  .back-name { left: 418px; top: 497px; font-family: var(--sans); font-weight: 600; font-size: 42px; line-height: 1; letter-spacing: 0.01em; text-transform: uppercase; white-space: nowrap; }
  .name-rule { left: 421px; top: 547px; width: 119px; height: 5px; background: var(--ink); }
  .detail-list { left: 400px; top: 561px; width: 400px; list-style: none; }
  .detail-row { display: flex; align-items: center; height: 21px; }
  .detail-role { width: 242px; text-align: right; font-family: var(--serif); font-size: 15px; text-transform: uppercase; }
  .detail-sep { width: 1.5px; height: 15px; background: var(--ink); margin: 0 6px 0 4px; }
  .detail-info { font-family: var(--sans); font-weight: 600; font-size: 12.5px; white-space: nowrap; }
</style>
</head>
<body>
<main class="stage">
  <section class="card card--front" aria-label="Business card front"></section>
  <div class="abs brand-mark" aria-hidden="true"></div>
  <p class="abs brand-name brand-name--front">Marlo<br>Vitality</p>
  <h1 class="abs front-name">TOMÁS ARRIBAL</h1>
  <p class="abs front-roles">Wellness Coach | Consultant | Trainer.</p>
  <p class="abs front-contact">marlovitality.example | (+34) 612 480 397 | Spain &nbsp;| +1 (555) 318 2046 | USA</p>

  <section class="card card--back" aria-label="Business card back"></section>
  <div class="abs edge-block edge-block--left"></div>
  <div class="abs edge-block edge-block--bottom"></div>
  <p class="abs brand-name brand-name--back">Marlo<br>Vitality</p>
  <h2 class="abs back-name">Tomás Arribal</h2>
  <div class="abs name-rule"></div>
  <ul class="abs detail-list">
    <li class="detail-row"><span class="detail-role">Wellness Coach</span><span class="detail-sep"></span><span class="detail-info">marlovitality.example</span></li>
    <li class="detail-row"><span class="detail-role">Consultant</span><span class="detail-sep"></span><span class="detail-info">(+34) 612 480 397 | Spain</span></li>
    <li class="detail-row"><span class="detail-role">Trainer</span><span class="detail-sep"></span><span class="detail-info">+1 (555) 318 2046 | USA</span></li>
  </ul>
</main>
</body>
</html>
```